BrindleWorks Business Card Design

Design business cards with attached ideas. I am open to several different ideas that would be interesting and innovative. What I have provided is logo and colors. Font should be Helvetica although it could be bold or light as needed. The design can be vertical or horizontal. The design should be more interesting than a standard business card. Files must be ready to send to a printer and in Illustrator format. The text with the five icons should be exact. Send me some ideas and I will get back to you right away. I need to choose a design within 3-5 days.

Target Market(s)

Business audience

Industry/Entity Type

Business

Contact Information for Business Card

Files should be ready to send to printer in illustrator format

Font styles to use
Sans Serif

Colors
3276b5

Requirements
Must have
• Use attached logo and two colors - blue / gray
• Include 5 offering icons and text on back
Nice to have
• Interesting and innovative design. Vertical or horizontal are both fine.

```html
<!DOCTYPE html>
<html lang="en">
<head>
<meta charset="utf-8">
<title>BrindleWorks Business Cards</title>
<link rel="stylesheet" href="https://fonts.googleapis.com/css2?family=Arimo:wght@400;700&display=swap">
<style>
  :root {
    --brand-blue: #3276b5;
    --brand-gray: #58585a;
    --ink: #222226;
    --paper: #ffffff;
    --backdrop: #e9e7e3;
    --rule: #9a9a9c;
  }
  * { margin: 0; padding: 0; box-sizing: border-box; }
  html, body { width: 1200px; height: 892px; overflow: hidden; }
  body {
    background: var(--backdrop);
    font-family: "Arimo", Helvetica, Arial, sans-serif;
    position: relative;
  }
  .card { position: absolute; background: var(--paper); box-shadow: 0 6px 18px rgba(0,0,0,.18); }

  /* Front, vertical */
  .card-front {
    left: 90px; top: 136px; width: 360px; height: 620px;
    background: var(--brand-blue);
    padding: 14px;
  }
  .front-inner { width: 100%; height: 100%; background: var(--paper); display: flex; flex-direction: column; }
  .brand-area {
    height: 276px; display: flex; flex-direction: column; align-items: center; justify-content: center; gap: 14px;
  }
  .brand-mark { width: 92px; height: 92px; background: var(--brand-gray); border-radius: 10px; }
  .brand-name { font-size: 44px; font-weight: 400; color: var(--brand-blue); letter-spacing: -0.5px; }
  .tagline { font-size: 16px; color: var(--ink); margin-top: -6px; }
  .contact-band { flex: 1; background: var(--brand-blue); padding: 12px; }
  .contact-frame {
    height: 100%; border: 3px solid var(--paper); color: var(--paper);
    display: flex; flex-direction: column; align-items: center; padding-top: 38px;
  }
  .person-name { font-size: 30px; font-weight: 700; letter-spacing: .5px; }
  .person-title { font-size: 18px; margin-top: 4px; }
  .divider { width: 80%; height: 1px; background: rgba(255,255,255,.8); margin: 16px 0 18px; }
  .contact-line { font-size: 18px; line-height: 1.45; }

  /* Back, horizontal */
  .card-back { left: 520px; top: 271px; width: 600px; height: 350px; padding: 26px 34px; }
  .back-header { display: flex; align-items: center; gap: 16px; padding-bottom: 12px; border-bottom: 2px solid var(--rule); }
  .back-mark { width: 46px; height: 46px; background: var(--brand-blue); }
  .back-title { font-size: 30px; font-weight: 400; color: var(--ink); }
  .offerings { list-style: none; margin-top: 20px; }
  .offering { display: flex; align-items: center; gap: 14px; font-size: 19px; color: var(--ink); height: 44px; }
  .offering-icon { width: 28px; height: 28px; flex: none; }
</style>
</head>
<body>

<section class="card card-front" aria-label="Business card front">
  <div class="front-inner">
    <div class="brand-area">
      <div class="brand-mark"></div>
      <div class="brand-name">BrindleWorks</div>
      <div class="tagline">Clear Plans - Steady Growth</div>
    </div>
    <div class="contact-band">
      <div class="contact-frame">
        <div class="person-name">Dana Hollis, PhD</div>
        <div class="person-title">Managing Director</div>
        <div class="divider"></div>
        <div class="contact-line">555-014-0296</div>
        <div class="contact-line">BrindleWorks.com</div>
        <div class="contact-line">Dana@BrindleWorks.com</div>
      </div>
    </div>
  </div>
</section>

<section class="card card-back" aria-label="Business card back">
  <header class="back-header">
    <div class="back-mark"></div>
    <h1 class="back-title">BrindleWorks Offerings</h1>
  </header>
  <ul class="offerings">
    <li class="offering">
      <svg class="offering-icon" viewBox="0 0 28 28"><circle cx="14" cy="14" r="14" fill="#3276b5"/><rect x="9" y="8" width="10" height="12" fill="none" stroke="#fff" stroke-width="1.6"/><path d="M11 12h6M11 15h6M11 18h4" stroke="#fff" stroke-width="1.3"/></svg>
      <span>Concepts: Thought leadership white papers</span>
    </li>
    <li class="offering">
      <svg class="offering-icon" viewBox="0 0 28 28"><circle cx="14" cy="14" r="14" fill="#3276b5"/><rect x="8" y="9" width="12" height="8" fill="none" stroke="#fff" stroke-width="1.6"/><path d="M14 17v3M10 20h8" stroke="#fff" stroke-width="1.6"/></svg>
      <span>Curriculum: Short courses on strategy</span>
    </li>
    <li class="offering">
      <svg class="offering-icon" viewBox="0 0 28 28"><circle cx="14" cy="14" r="14" fill="#3276b5"/><circle cx="14" cy="11" r="3" fill="#fff"/><path d="M8 20c1-4 11-4 12 0z" fill="#fff"/></svg>
      <span>Coaching: Building your strategic leadership</span>
    </li>
    <li class="offering">
      <svg class="offering-icon" viewBox="0 0 28 28"><circle cx="14" cy="14" r="14" fill="#3276b5"/><path d="M8 18l4-4 3 3 5-6" fill="none" stroke="#fff" stroke-width="1.8"/><path d="M17 11h3v3" fill="none" stroke="#fff" stroke-width="1.6"/></svg>
      <span>Coaching: Developing your strategic future</span>
    </li>
    <li class="offering">
      <svg class="offering-icon" viewBox="0 0 28 28"><circle cx="14" cy="14" r="14" fill="#3276b5"/><path d="M9 19v-4M13 19v-7M17 19v-5M21 19v-9" stroke="#fff" stroke-width="2"/></svg>
      <span>ScoreCard: Balanced scorecard and software</span>
    </li>
  </ul>
</section>

</body>
</html>
```